FOR SALE sign for REAL ESTATE BROKERAGE

Hello - our sign is attached. Need to make it part of FOR SALE sign. Think TERA/VOX, Dunmore Pratt, Foxglen Ashworth. Needs to have logo + FOR SALE + company website and phone number Its 24 x 30 standard size Needs to be MODERN yet luxury / sophisticated. Colors = red, black, gray, white (any mix). Will be used all over Philadelphia + surrounding areas. Please do Qwindle Image search on FOR SALE SIGNGS for some top comanies- Tera/vox, dunmore pratt, foxglen ashworth *** please mock-up the sign in front of a house

Target Market(s)

People with $$

Industry/Entity Type

Real Estate

Font styles to use
Sans Serif

Colors
ec1f27
ffffff
000000
5c5c5c

Requirements
Must have
• logo, website (tallpinehomes.example) phone number 555-014-7390 Agent name: Dorin Maklasov

```html
<!DOCTYPE html>
<html lang="en">
<head>
<meta charset="UTF-8">
<title>For Sale Sign – Tallpine Homes Inc.</title>
<link rel="stylesheet" href="https://fonts.googleapis.com/css2?family=Lato:wght@400;700;900&display=swap">
<style>
  :root {
    --red: #c21d2e;
    --black: #231f20;
    --white: #ffffff;
    --gray: #5c5c5c;
    --page: #ffffff;
  }
  * { margin: 0; padding: 0; box-sizing: border-box; }
  html, body {
    width: 803px;
    height: 1200px;
    overflow: hidden;
    background: var(--page);
    font-family: "Lato", sans-serif;
  }
  .canvas {
    position: relative;
    width: 803px;
    height: 1200px;
  }
  .sign {
    position: absolute;
    left: 51px;
    top: 320px;
    width: 700px;
    height: 560px;
    background: var(--white);
    box-shadow: 0 4px 14px rgba(0, 0, 0, 0.28);
    display: flex;
    flex-direction: column;
    overflow: hidden;
  }
  .sign__headline {
    height: 161px;
    background: var(--black);
    color: var(--white);
    font-weight: 700;
    font-size: 130px;
    line-height: 161px;
    text-align: center;
    letter-spacing: -1px;
  }
  .sign__body {
    position: relative;
    flex: 1;
    display: flex;
    flex-direction: column;
    align-items: center;
  }
  .member-badge {
    position: absolute;
    top: 12px;
    right: 44px;
    width: 22px;
    height: 22px;
    background: var(--black);
  }
  .brand {
    margin-top: 52px;
    display: flex;
    align-items: center;
    gap: 14px;
  }
  .brand__square {
    width: 34px;
    height: 34px;
    background: var(--red);
  }
  .brand__name {
    color: var(--red);
    font-weight: 900;
    font-size: 52px;
    letter-spacing: -1px;
    line-height: 1;
  }
  .contact__phone {
    margin-top: 58px;
    color: var(--black);
    font-weight: 700;
    font-size: 57px;
    line-height: 1;
  }
  .contact__web {
    margin-top: 8px;
    color: var(--black);
    font-weight: 700;
    font-size: 31px;
    line-height: 1;
  }
  .contact__web .domain { color: var(--red); }
  .sign__agent {
    height: 97px;
    background: var(--red);
    color: var(--white);
    display: flex;
    align-items: baseline;
    justify-content: center;
    padding-top: 14px;
    font-weight: 700;
  }
  .agent__name { font-size: 60px; letter-spacing: -0.5px; }
  .agent__title { font-size: 30px; margin-left: 6px; }
</style>
</head>
<body>
  <main class="canvas">
    <section class="sign" aria-label="For sale yard sign">
      <header class="sign__headline">FOR SALE</header>
      <div class="sign__body">
        <span class="member-badge" aria-hidden="true"></span>
        <div class="brand">
          <span class="brand__square" aria-hidden="true"></span>
          <span class="brand__name">Tallpine Homes Inc.</span>
        </div>
        <p class="contact__phone">555-014-7390</p>
        <p class="contact__web">www.<span class="domain">tallpinehomes</span>.example</p>
      </div>
      <footer class="sign__agent">
        <span class="agent__name">Dorin Maklasov,</span>
        <span class="agent__title">Realtor</span>
      </footer>
    </section>
  </main>
</body>
</html>
```